Spice Mix Label Bottle Branding - Health and Weight Loss Mixes

The company is called ZestRow Spice Mix's. We've created 5 spice mixes using ingredients that promote health and weight loss. We already have a logo but now we need labels for our bottles. We would like to see designs that have the feel of health supplements (see attached examples)

We would like a different colour featured with each of our flavours.

Our flavours are:
-Golden Chai (Yellow)
-Mild Curry (Orange)
-Coffee Rub (brown)
-Garlic Oregano (Green)
-Taco (Blue)

Thank you!

Target Market(s)

Ages 22-35. Men and Female. Trendy, Hipster.

Industry/Entity Type

Food Production

Font styles to use
Sans Serif

Colors
f37122
0655a3
0692cd
9bcb3c
fbee3f

Requirements
Must have
• A different featured colour for each flavour.
• The ZestRow Spices Logo (attached)
• The slogan: "Weight Loss Ingredients"
• -Golden Chai (Yellow)
• -Mild Curry (Orange)
• -Coffee Rub (brown)
• -Garlic Oregano (Green)
• -Taco (Blue)
• Text Files attached.
Nice to have
• A black label with a featured colour for each of the spice mice flavours.
• 'No Salt added'

```html
<!DOCTYPE html>
<html lang="en">
<head>
<meta charset="utf-8">
<title>ZestRow Spices – Bottle Labels</title>
<link rel="stylesheet" href="https://fonts.googleapis.com/css2?family=Poppins:ital,wght@0,600;0,700;0,800;1,400;1,500&display=swap">
<style>
  :root {
    --page: #ffffff;
    --label-black: #000000;
    --label-white: #ffffff;
    --curry: #ef5a24;
    --taco: #1a9ad6;
    --chai: #d49a2a;
    --garlic: #9ab83e;
    --coffee: #8d5e2f;
    --font: "Poppins", sans-serif;
  }
  * { box-sizing: border-box; margin: 0; padding: 0; }
  html, body {
    width: 1200px; height: 960px; overflow: hidden;
    background: var(--page);
    font-family: var(--font);
  }
  .sheet { position: relative; width: 1200px; height: 960px; }

  .label {
    position: absolute;
    width: 368px; height: 384px;
    color: var(--label-white);
  }
  .label__shape { position: absolute; inset: 0; width: 100%; height: 100%; }
  .label__shape .edge { fill: var(--label-black); }
  .label__shape .ring { fill: none; stroke: var(--label-white); stroke-width: 3; stroke-linejoin: round; }
  .label__shape .trim { fill: none; stroke: var(--accent); stroke-width: 2.6; stroke-linejoin: round; }

  .brand {
    position: absolute; left: 0; right: 0; top: 40px;
    display: flex; flex-direction: column; align-items: center;
  }
  .brand__dot {
    width: 16px; height: 16px; border-radius: 50%;
    background: var(--accent); margin-bottom: 4px;
  }
  .brand__name {
    font-weight: 800; color: var(--label-white);
    text-align: center; line-height: 1;
    font-size: 30px; letter-spacing: -0.5px;
  }
  .brand__name small { display: block; font-size: 11px; letter-spacing: 4px; margin-top: 3px; }

  .flavour {
    position: absolute; left: 17px; width: 335px;
    background: var(--accent); color: var(--label-black);
    display: flex; align-items: center; justify-content: center;
    text-align: center; font-weight: 800; text-transform: uppercase;
    line-height: 1; letter-spacing: 0.5px;
  }
  .slogan, .claim, .weight {
    position: absolute; left: 0; right: 0; text-align: center;
  }
  .slogan { color: var(--accent); font-style: italic; font-weight: 400; font-size: 17px; }
  .claim { font-weight: 600; font-size: 11.5px; }
  .weight { font-weight: 700; font-size: 13px; line-height: 18px; }

  .label--curry  { --accent: var(--curry);  left: 22px;  top: 84px; }
  .label--taco   { --accent: var(--taco);   left: 418px; top: 84px; }
  .label--chai   { --accent: var(--chai);   left: 814px; top: 84px; }
  .label--garlic { --accent: var(--garlic); left: 214px; top: 516px; }
  .label--coffee { --accent: var(--coffee); left: 622px; top: 516px; }

  .label--standard .flavour { top: 156px; height: 66px; font-size: 44px; }
  .label--standard .slogan  { top: 234px; }
  .label--standard .claim   { top: 275px; }
  .label--standard .weight  { top: 306px; }
  .label--chai .flavour { font-size: 40px; }

  .label--garlic .flavour { top: 144px; height: 90px; font-size: 40px; flex-direction: column; }
  .label--garlic .slogan  { top: 245px; }
  .label--garlic .claim   { top: 274px; }
  .label--garlic .weight  { top: 300px; }

  .label--coffee .flavour { top: 150px; height: 66px; font-size: 43px; }
  .label--coffee .slogan  { top: 229px; }
  .label--coffee .claim   { top: 270px; }
  .label--coffee .weight  { top: 300px; }
</style>
</head>
<body>
<main class="sheet">

  <article class="label label--standard label--curry">
    <svg class="label__shape" viewBox="0 0 307 320" aria-hidden="true">
      <polygon class="edge" points="95,2 212,2 305,60 305,260 212,318 95,318 2,260 2,60"/>
      <polygon class="ring" points="97,7 210,7 300,63 300,257 210,313 97,313 7,257 7,63"/>
      <polygon class="trim" points="100,14 207,14 293,67 293,253 207,306 100,306 14,253 14,67"/>
    </svg>
    <div class="brand"><span class="brand__dot"></span><p class="brand__name">ZestRow<small>SPICES</small></p></div>
    <h2 class="flavour">Mild Curry</h2>
    <p class="slogan">Weight Loss Ingredients</p>
    <p class="claim">NO SALT</p>
    <p class="weight">Net Wt.<br>10,5 oz</p>
  </article>

  <article class="label label--standard label--taco">
    <svg class="label__shape" viewBox="0 0 307 320" aria-hidden="true">
      <polygon class="edge" points="95,2 212,2 305,60 305,260 212,318 95,318 2,260 2,60"/>
      <polygon class="ring" points="97,7 210,7 300,63 300,257 210,313 97,313 7,257 7,63"/>
      <polygon class="trim" points="100,14 207,14 293,67 293,253 207,306 100,306 14,253 14,67"/>
    </svg>
    <div class="brand"><span class="brand__dot"></span><p class="brand__name">ZestRow<small>SPICES</small></p></div>
    <h2 class="flavour">Taco</h2>
    <p class="slogan">Weight Loss Ingredients</p>
    <p class="claim">NO SALT</p>
    <p class="weight">Net Wt.<br>10,5 oz</p>
  </article>

  <article class="label label--standard label--chai">
    <svg class="label__shape" viewBox="0 0 307 320" aria-hidden="true">
      <polygon class="edge" points="95,2 212,2 305,60 305,260 212,318 95,318 2,260 2,60"/>
      <polygon class="ring" points="97,7 210,7 300,63 300,257 210,313 97,313 7,257 7,63"/>
      <polygon class="trim" points="100,14 207,14 293,67 293,253 207,306 100,306 14,253 14,67"/>
    </svg>
    <div class="brand"><span class="brand__dot"></span><p class="brand__name">ZestRow<small>SPICES</small></p></div>
    <h2 class="flavour">Golden Chai</h2>
    <p class="slogan">Weight Loss Ingredients</p>
    <p class="claim">NO SALT</p>
    <p class="weight">Net Wt.<br>10,5 oz</p>
  </article>

  <article class="label label--garlic">
    <svg class="label__shape" viewBox="0 0 307 320" aria-hidden="true">
      <polygon class="edge" points="95,2 212,2 305,60 305,260 212,318 95,318 2,260 2,60"/>
      <polygon class="ring" points="97,7 210,7 300,63 300,257 210,313 97,313 7,257 7,63"/>
      <polygon class="trim" points="100,14 207,14 293,67 293,253 207,306 100,306 14,253 14,67"/>
    </svg>
    <div class="brand"><span class="brand__dot"></span><p class="brand__name">ZestRow<small>SPICES</small></p></div>
    <h2 class="flavour"><span>Garlic</span><span>Oregano</span></h2>
    <p class="slogan">Weight Loss Ingredients</p>
    <p class="claim">NO SALT</p>
    <p class="weight">Net Wt.<br>10,5 oz</p>
  </article>

  <article class="label label--coffee">
    <svg class="label__shape" viewBox="0 0 307 320" aria-hidden="true">
      <polygon class="edge" points="95,2 212,2 305,60 305,260 212,318 95,318 2,260 2,60"/>
      <polygon class="ring" points="97,7 210,7 300,63 300,257 210,313 97,313 7,257 7,63"/>
      <polygon class="trim" points="100,14 207,14 293,67 293,253 207,306 100,306 14,253 14,67"/>
    </svg>
    <div class="brand"><span class="brand__dot"></span><p class="brand__name">ZestRow<small>SPICES</small></p></div>
    <h2 class="flavour">Coffee Rub</h2>
    <p class="slogan">Weight Loss Ingredients</p>
    <p class="claim">NO SALT</p>
    <p class="weight">Net Wt.<br>10,5 oz</p>
  </article>

</main>
</body>
</html>
```